Designer Needed for Protein Label

We are looking for an experienced graphic designer to create a label for our protein supplement Quill ISOLATE 100% WHEY Protein 3LB tub. You can make it unique to our design but keep it clean and simple.

Here are some design examples that we liked, however please note ours is unflavored:

https://www.brantova.com/VelnorFit-Tundra-Protein-Powder-Chocolate/dp/K47RQWZ2NX/ref=sr_1_17_a_it?ie=UTF8&qid=1536255229&sr=8-17&keywords=protein%2Bpowder&th=1

https://www.brantova.com/dp/K93TLMQ5VB/ref=sspa_dk_detail_1?pd_rd_i=K93TLMQ5VB&pf_rd_m=QWERTYPLMNB&pf_rd_p=7c1402ab-816e-4a2c-9e3f-27a4c188f3d1&pf_rd_r=HJKWPLZNRT8VQC217DMS&pd_rd_wg=TrQ4k&pf_rd_s=desktop-dp-sims&pf_rd_t=40701&pd_rd_w=KLMN3&pf_rd_i=desktop-dp-sims&pd_rd_r=917f3a21-c2de-11e8-942a-ab17fd2249c7&th=1

Please see attachment for Quill Logo and additional label example.

Label Dimensions:
18in x 6in

Please include the following information on the label:
* Quill Icon
* ISOLATE - product name
* 100% WHEY Protein
* Unflavored
* Net WT. 3LB (1.36 KG)
* 40 Servings
* 50 Grams of Protein per serving
* XX  BCAA
* Gluten & Lactose Free
* Kosher and Halal Certified
* Non GMO
* Nutrition Facts (use as place holder)
* Ingredients
* Directions
* Barcode

```html
<!DOCTYPE html>
<html lang="en">
<head>
<meta charset="utf-8">
<title>Quill ISOLATE 100% Whey Protein – Label</title>
<link href="https://fonts.googleapis.com/css2?family=Oswald:wght@300;400;500&family=Roboto:wght@400;700&family=Roboto+Condensed:wght@300;400;700&display=swap" rel="stylesheet">
<style>
  :root{
    --bg:#e9e9e9;
    --label:#3b3b3d;
    --label-dark:#2e2e30;
    --yellow:#f3e500;
    --white:#f4f4f4;
    --muted:#bdbdbd;
    --ink:#111;
  }
  *{box-sizing:border-box;margin:0;padding:0}
  html,body{width:1200px;height:728px;overflow:hidden;background:var(--bg)}
  body{font-family:"Roboto",Arial,sans-serif;color:var(--white)}
  .label{position:absolute;left:30px;top:174px;width:1140px;height:380px;background:var(--label);display:grid;grid-template-columns:380px 380px 380px}
  .panel{position:relative;height:380px;overflow:hidden}
  .panel--front{background:var(--label-dark)}

  /* left claims panel */
  .claims{position:absolute;left:22px;top:30px;display:flex;gap:6px;font-family:"Oswald",sans-serif;line-height:1}
  .claims__side{display:flex;flex-direction:column;align-items:center;width:26px}
  .claims__num{font-size:28px;font-weight:500}
  .claims__tiny{font-size:6px;letter-spacing:.5px}
  .vertical{writing-mode:vertical-rl;transform:rotate(180deg)}
  .claims__protein{font-size:25px;margin:3px 0}
  .claims__main{display:flex;flex-direction:column;gap:4px;border-left:1px solid var(--white);border-right:1px solid var(--white);padding:0 6px}
  .row{display:flex;align-items:center;gap:4px}
  .big{font-size:40px;font-weight:500;letter-spacing:-1px}
  .mid{font-size:23px;font-weight:400;letter-spacing:-.5px}
  .stack{display:flex;flex-direction:column;font-size:15px;line-height:.95}
  .stack--tiny{font-size:11px}
  .stack--tiny small{font-size:5px}
  .free{font-size:62px;font-weight:500;letter-spacing:-1px}
  .claims__instant{font-size:25px}
  .motto{position:absolute;left:22px;top:214px;font-family:"Oswald",sans-serif;font-size:20px;letter-spacing:.2px}
  .blurb{position:absolute;left:22px;top:246px;width:320px}
  .blurb h3{font-size:10px;font-weight:400;margin-bottom:2px}
  .blurb p{font-size:6.5px;line-height:1.3;color:var(--muted)}
  .badges{position:absolute;left:22px;top:284px;display:flex;gap:14px}
  .badge{display:flex;flex-direction:column;align-items:center;gap:3px;font-size:7px;color:var(--yellow)}
  .badge span{display:block;width:22px;height:22px;border-radius:50%;border:2px solid var(--yellow)}
  .barcode-slot{position:absolute;left:22px;top:326px;width:140px;height:30px;background:var(--yellow);color:var(--ink);font-family:"Oswald",sans-serif;font-weight:500;font-size:9px;letter-spacing:1px;display:flex;align-items:center;padding-left:30px}

  /* front panel */
  .mascot{position:absolute;left:118px;top:12px;width:58px;height:58px;background:linear-gradient(180deg,#f3e500,#c9bd00);border-radius:30px 30px 10px 10px}
  .mascot-shadow{position:absolute;left:55px;top:190px;width:110px;height:130px;background:#343436;border-radius:55px 55px 20px 20px}
  .brand{position:absolute;left:18px;top:74px;display:flex;align-items:center;gap:8px}
  .brand__mark{width:16px;height:16px;background:var(--yellow)}
  .brand__name{font-family:"Oswald",sans-serif;font-weight:500;font-size:42px;color:var(--yellow);letter-spacing:1px;line-height:1}
  .flavor{position:absolute;left:28px;top:132px;font-family:"Oswald",sans-serif;font-weight:500;font-size:17px;color:var(--yellow);letter-spacing:1px}
  .flavor::after{content:"";display:block;width:126px;height:2px;background:var(--yellow);margin-top:3px}
  .v{position:absolute;top:18px;height:300px;writing-mode:vertical-rl;transform:rotate(180deg);font-family:"Oswald",sans-serif;line-height:1;white-space:nowrap}
  .isolate{left:222px;font-size:90px;font-weight:300;color:var(--yellow)}
  .rule{position:absolute;top:22px;width:2px;height:296px;background:var(--yellow)}
  .rule--a{left:300px}
  .rule--b{left:342px}
  .whey{left:305px;font-size:34px;font-weight:300;color:var(--white)}
  .servings{left:347px;font-size:15px;font-weight:300;color:var(--yellow)}
  .servings small{font-family:"Roboto",sans-serif;font-size:10px}
  .netwt{position:absolute;left:222px;top:344px;font-family:"Roboto Condensed",sans-serif;font-weight:300;font-size:15px}

  /* back panel */
  .facts{position:absolute;left:22px;top:24px;width:186px;background:#fff;color:var(--ink);padding:4px 5px;font-size:5.5px;line-height:1.35}
  .facts h2{font-family:"Roboto",sans-serif;font-weight:700;font-size:17px;line-height:1;border-bottom:1px solid var(--ink);padding-bottom:2px}
  .facts .thick{border-bottom:4px solid var(--ink)}
  .facts .line{display:flex;justify-content:space-between;border-bottom:.5px solid #888}
  .facts .note{margin-top:2px;font-size:5px}
  .ingr-side{position:absolute;left:218px;top:22px;width:150px;font-size:7px;line-height:1.35;color:var(--white)}
  .ingr-side b{font-size:10px;font-weight:400}
  .back-copy{position:absolute;left:22px;top:226px;width:340px;font-size:7.5px;line-height:1.3}
  .back-copy p{margin-bottom:6px}
</style>
</head>
<body>
<main class="label">

  <section class="panel panel--claims">
    <div class="claims">
      <div class="claims__side">
        <div class="claims__num">50</div>
        <div class="claims__tiny">GRAMS</div>
        <div class="claims__protein vertical">PROTEIN</div>
        <div class="claims__tiny">PER</div>
        <div class="claims__tiny">SERVING</div>
      </div>
      <div class="claims__main">
        <div class="row"><span class="big">100% WHEY</span><span class="stack"><span>PROTEIN</span><span>ISOLATE</span></span></div>
        <div class="row"><span class="mid">10,900 MG BCAA'S</span><span class="stack stack--tiny"><span>PER</span><small>SERVING</small></span></div>
        <div class="row"><span class="mid">4.6G L-GLUTAMINE</span><span class="stack stack--tiny"><span>PER</span><small>SERVING</small></span></div>
        <div class="row"><span class="stack"><span>GLUTEN</span><span>LACTOSE</span><span>ASPARTAME</span></span><span class="free">FREE</span></div>
      </div>
      <div class="claims__instant vertical">INSTANTIZED</div>
    </div>
    <p class="motto">WE'RE ALL MORE THAN MUSCLE</p>
    <div class="blurb">
      <h3>Pure Naked Protein</h3>
      <p>Lorem ipsum dolor sit amet, consectetuer adipiscing elit, sed diam nonummy nibh euismod tincidunt ut laoreet dolore magna aliquam erat volutpat. Ut wisi enim ad minim veniam,</p>
    </div>
    <div class="badges">
      <div class="badge"><span></span>Gluten Free</div>
      <div class="badge"><span></span>Lactose Free</div>
      <div class="badge"><span></span>Kosher Certified</div>
      <div class="badge"><span></span>Halal Certified</div>
      <div class="badge"><span></span>Non GMO</div>
    </div>
    <div class="barcode-slot">BAR CODE</div>
  </section>

  <section class="panel panel--front">
    <div class="mascot-shadow" role="img" aria-label="Faint brand mascot silhouette"></div>
    <div class="mascot" role="img" aria-label="Brand mascot illustration in yellow"></div>
    <div class="brand"><span class="brand__mark"></span><span class="brand__name">QUILL</span></div>
    <p class="flavor">UNFLAVORED</p>
    <h1 class="v isolate">ISOLATE</h1>
    <span class="rule rule--a"></span>
    <p class="v whey">100% WHEY PROTEIN</p>
    <span class="rule rule--b"></span>
    <p class="v servings">40 SERVINGS | <small>50 Grams of Protein per serving</small></p>
    <p class="netwt">Net WT. 3LB (1.36 KG)</p>
  </section>

  <section class="panel panel--back">
    <div class="facts">
      <h2>Nutrition Facts</h2>
      <div class="line"><span>Serving Size 1 Scoop (34g)</span></div>
      <div class="line thick"><span>Servings Per Container 40</span></div>
      <div class="line"><b>Amount Per Serving</b></div>
      <div class="line"><span>Calories 130</span><span>Calories from Fat 10</span></div>
      <div class="line"><span></span><b>% Daily Value*</b></div>
      <div class="line"><span>Total Fat 1g</span><span>2%</span></div>
      <div class="line"><span>Total Carbohydrate 3g</span><span>1%</span></div>
      <div class="line"><span>Cholesterol 10mg</span><span>3%</span></div>
      <div class="line"><span>Sodium 90mg</span><span>4%</span></div>
      <div class="line"><span>Potassium 200mg</span><span>6%</span></div>
      <div class="line thick"><b>Protein 50g</b><span></span></div>
      <div class="line"><span>Calcium 10%</span><span>Iron 2%</span></div>
      <p class="note">*Percent Daily Values are based on a 2,000 calorie diet.</p>
    </div>
    <p class="ingr-side"><b>Ingredients:</b> Lorem ipsum dolor sit amet, consectetuer adipiscing elit, sed diam nonummy nibh euismod tincidunt ut laoreet dolore magna aliquam erat volutpat. Ut wisi enim ad minim veniam, quis nostrud exerci tation ullamcorper suscipit lobortis nisl ut aliquip ex ea commodo consequat. Duis autem vel eum iriure dolor in hendrerit in vulputate velit esse molestie consequat, vel illum dolore eu feugiat nulla facilisis at vero eros et accumsan et iusto odio dignissim qui blandit praesent luptatum zzril delenit augue duis dolore te feugait nulla facilisi.</p>
    <div class="back-copy">
      <p>Ingredients: Lorem ipsum dolor sit amet, consectetuer adipiscing elit, sed diam nonummy nibh euismod tincidunt ut laoreet dolore magna aliquam erat volutpat. Ut wisi enim ad</p>
      <p>Contains: Milk and Soy.</p>
      <p>Manufactured for: Lorem ipsum dolor sit amet, consectetuer adipiscing elit, sed diam nonummy nibh euismod tincidunt ut laoreet dolore magna aliquam erat volutpat. Ut wisi enim ad</p>
      <p>Contents sold by weight, not volume, keep in a cool, dry place.</p>
      <p>Made in the USA- This product contains ingredients of international and domestic arigin</p>
    </div>
  </section>

</main>
</body>
</html>
```